Album Single Song Cover Art Needed - Hip-Hop, Pop, R&B Artist

Need a CD "Single Release" Cover Art designed for Native American Hip Hop Artist - K Velour. Template: Platewright - 300ppi. Two separate Art Designs - One with no wording; the other with Wording. Single Song Title is: Too Golden / Artist: K Velour. Thoughts on artwork - Close Up of Face, create a vision of "Fierce". Looking to make a powerful statement - colors vibrant, splashy. Let your creativity run free - whatever "FIERCE" comes to mind, etc., Let me see what you can do. I provided a couple of pictures - take your pick of any to use - remove background. Happy designing!
Updates

Would like to see a few more designs come through as well as allow you to create additional designs. Thank you.

Target Market(s)

Music, Entertainment

Industry/Entity Type

Music, Entertainment

Font styles to use
Other font styles liked:
• Let the Designer Choose

Requirements
Must have
• FIERCE
Nice to have
• Vibrant, Color, Splashes - think "FIERCE"

```html
<!DOCTYPE html>
<html lang="en">
<head>
<meta charset="utf-8">
<title>Too Golden – K Velour single cover</title>
<link rel="stylesheet" href="https://fonts.googleapis.com/css2?family=Rubik+Dirt&display=swap">
<style>
  :root {
    --page: #ffffff;
    --red: #f2141c;
    --orange: #ffa812;
    --amber: #ffc21a;
    --cyan: #22d6f2;
    --magenta: #ff1a78;
    --ink: #141414;
    --paper: #ffffff;
    --title-yellow: #ffe21c;
    --artist-white: #ffffff;
  }
  html, body {
    margin: 0;
    padding: 0;
    width: 1200px;
    height: 1200px;
    overflow: hidden;
    background: var(--page);
  }
  .canvas {
    position: relative;
    width: 1200px;
    height: 1200px;
  }
  .cover {
    position: absolute;
    overflow: hidden;
  }
  .cover--titled {
    left: 308px;
    top: 106px;
    width: 572px;
    height: 571px;
  }
  .cover--plain {
    left: 421px;
    top: 734px;
    width: 360px;
    height: 359px;
  }
  .cover__art {
    position: absolute;
    inset: 0;
    background:
      radial-gradient(ellipse 28% 30% at 46% 34%, rgba(255,255,255,0.75), rgba(255,255,255,0) 70%),
      radial-gradient(ellipse 22% 18% at 58% 72%, rgba(255,255,255,0.85), rgba(255,255,255,0) 75%),
      radial-gradient(ellipse 35% 40% at 92% 62%, var(--cyan), rgba(34,214,242,0) 75%),
      radial-gradient(ellipse 40% 30% at 40% 85%, var(--magenta), rgba(255,26,120,0) 75%),
      radial-gradient(ellipse 45% 45% at 12% 22%, var(--red), rgba(242,20,28,0) 75%),
      radial-gradient(ellipse 30% 25% at 95% 92%, #1a1a1a, rgba(26,26,26,0) 75%),
      linear-gradient(135deg, var(--red) 0%, var(--orange) 45%, var(--amber) 60%, var(--orange) 100%);
  }
  .cover__type {
    position: absolute;
    inset: 0;
    width: 100%;
    height: 100%;
  }
  .cover__title,
  .cover__artist {
    font-family: "Rubik Dirt", "Impact", sans-serif;
  }
  .cover__title {
    fill: var(--title-yellow);
    font-size: 118px;
  }
  .cover__artist {
    fill: var(--artist-white);
    font-size: 80px;
  }
</style>
</head>
<body>
  <main class="canvas">
    <section class="cover cover--titled">
      <div class="cover__art" role="img" aria-label="Splashy spray-paint portrait illustration in red, orange, magenta and cyan"></div>
      <svg class="cover__type" viewBox="0 0 572 571" aria-hidden="false">
        <text class="cover__title" x="17" y="550" textLength="537" lengthAdjust="spacingAndGlyphs">TOO GOLDEN</text>
        <text class="cover__artist" transform="translate(482 20) rotate(90)" x="0" y="0" textLength="405" lengthAdjust="spacingAndGlyphs">K VELOUR</text>
      </svg>
    </section>

    <section class="cover cover--plain">
      <div class="cover__art" role="img" aria-label="Same splashy spray-paint portrait illustration without wording"></div>
    </section>
  </main>
</body>
</html>
```